Business Card front and back

I am looking for business card design. I really really like the design file I uploaded named 627788_19250069_3478263_85f427ee_image

Target Market(s)

Corporate Fitness High end Private country club

Industry/Entity Type

Fitness Industry

Contact Information for Business Card

The last image I like as an example I uploaded a bunch of my logos. The file labeled "the signature" is my business card information for you to use

Colors
0054AA
0677BA
7BADD7
CADEEF
E8F1F8

Requirements
Must have
• E-mail sigThe file I uploaded labeled "627788_19250069_3478263_85f427ee_image" with all the plus signs on the back if those could be the logo symbol I uploaded labeled "1 back.png"

```html
<!DOCTYPE html>
<html lang="en">
<head>
<meta charset="utf-8">
<title>Stride By Form – Business Card</title>
<link rel="stylesheet" href="https://fonts.googleapis.com/css2?family=Montserrat:wght@400;500;700;800&display=swap">
<style>
  :root {
    --page: #3a3a3a;
    --paper: #ffffff;
    --ink: #232323;
    --ink-soft: #333333;
    --brand-blue: #4a7fc4;
    --card-dark: #262626;
    --photo-top: #3b3b3b;
    --photo-bottom: #1c1c1c;
  }
  * { box-sizing: border-box; margin: 0; padding: 0; }
  html, body { width: 1200px; height: 1200px; overflow: hidden; }
  body {
    background: var(--page);
    font-family: "Montserrat", sans-serif;
    position: relative;
  }
  .card {
    position: absolute;
    left: 190px;
    width: 820px;
    height: 469px;
    border-radius: 34px;
    overflow: hidden;
  }
  .card--front { top: 100px; background: var(--paper); }
  .card--back { top: 630px; background: var(--card-dark); }

  /* front */
  .card__bands { position: absolute; left: 0; bottom: 0; width: 820px; height: 140px; }
  .profile {
    position: absolute; left: 110px; top: 88px;
    width: 190px; height: 190px; border-radius: 50%;
    border: 4px solid var(--brand-blue);
    background: radial-gradient(circle at 50% 40%, var(--photo-top), var(--photo-bottom));
  }
  .person {
    position: absolute; left: 40px; top: 300px; width: 330px;
    text-align: center;
  }
  .person__name {
    font-weight: 800; font-size: 34px; color: var(--brand-blue);
    letter-spacing: 0.5px; line-height: 1; white-space: nowrap;
  }
  .person__role {
    font-weight: 500; font-size: 16px; color: var(--ink);
    letter-spacing: 1.5px; margin-top: 8px;
  }
  .brand {
    position: absolute; display: flex; align-items: center; gap: 12px;
  }
  .brand__mark { background: var(--brand-blue); flex: none; }
  .brand__name { font-weight: 800; letter-spacing: 1px; white-space: nowrap; }
  .card--front .brand { left: 430px; top: 70px; }
  .card--front .brand__mark { width: 26px; height: 26px; }
  .card--front .brand__name { font-size: 27px; color: var(--ink); }

  .contact { position: absolute; left: 450px; top: 150px; list-style: none; }
  .contact__item {
    display: flex; align-items: center; gap: 12px;
    font-size: 19px; color: var(--ink-soft); height: 36px; white-space: nowrap;
  }
  .contact__icon { width: 22px; height: 22px; flex: none; }

  /* back */
  .card--back .brand { left: 0; right: 0; top: 200px; justify-content: center; }
  .card--back .brand__mark { width: 46px; height: 46px; }
  .card--back .brand__name { font-size: 52px; color: #ffffff; }
</style>
</head>
<body>

<section class="card card--front" aria-label="Card front">
  <svg class="card__bands" viewBox="0 0 820 140" aria-hidden="true">
    <polygon points="0,120 520,120 540,100 540,140 0,140" fill="var(--brand-blue)"/>
    <polygon points="552,84 820,84 820,140 552,140" fill="var(--ink)"/>
  </svg>

  <div class="profile" role="img" aria-label="Portrait photo of the consultant"></div>

  <div class="person">
    <div class="person__name">DAN HOLBROOK</div>
    <div class="person__role">CONSULTANT</div>
  </div>

  <div class="brand">
    <span class="brand__mark"></span>
    <span class="brand__name">STRIDE BY FORM</span>
  </div>

  <ul class="contact">
    <li class="contact__item">
      <svg class="contact__icon" viewBox="0 0 24 24"><path fill="var(--brand-blue)" d="M6.6 10.8a15 15 0 0 0 6.6 6.6l2.2-2.2c.3-.3.7-.4 1-.2 1.1.4 2.3.6 3.6.6.6 0 1 .4 1 1V20c0 .6-.4 1-1 1A17 17 0 0 1 3 4c0-.6.4-1 1-1h3.5c.6 0 1 .4 1 1 0 1.3.2 2.5.6 3.6.1.3 0 .7-.2 1z"/></svg>
      555-014-2870
    </li>
    <li class="contact__item">
      <svg class="contact__icon" viewBox="0 0 24 24"><rect x="2" y="5" width="20" height="14" fill="var(--brand-blue)"/><polyline points="2,5 12,13 22,5" fill="none" stroke="#fff" stroke-width="1.6"/></svg>
      dan@stridebyform.co
    </li>
    <li class="contact__item">
      <svg class="contact__icon" viewBox="0 0 24 24" fill="none" stroke="var(--brand-blue)" stroke-width="1.8"><circle cx="12" cy="12" r="10"/><ellipse cx="12" cy="12" rx="4.5" ry="10"/><line x1="2" y1="12" x2="22" y2="12"/></svg>
      www.stridebyform.co
    </li>
    <li class="contact__item">
      <svg class="contact__icon" viewBox="0 0 24 24"><path fill="var(--brand-blue)" d="M12 2a7 7 0 0 0-7 7c0 5 7 13 7 13s7-8 7-13a7 7 0 0 0-7-7zm0 9.5a2.5 2.5 0 1 1 0-5 2.5 2.5 0 0 1 0 5z"/></svg>
      Serving the Northern Plains
    </li>
  </ul>
</section>

<section class="card card--back" aria-label="Card back">
  <div class="brand">
    <span class="brand__mark"></span>
    <span class="brand__name">STRIDE BY FORM</span>
  </div>
</section>

</body>
</html>
```